International Manufacturing Business Needs A Heavy Hitting Wordpress Design!

We need wordpress template designs for a new website for our UK based International company Tolvane Engineering Ltd. We manufacture and supply steel security doors and window units. We would like designs that feature the black and yellow industrial "stripes" that can be seen at our current site www.tolvadoors.com. The final design should communicate strength, power and weight to represent the quality of the products and the security that they provide.

It feels like we need 3 different types of page to be able to be created as per the current website at www.tolvasecuredoors.com.

Homepage
Products/Accessories
Leadtimes/Downloads/Contact

It may be that 3 different page types can be created with one template. I'm totally open to this.

I don't like the way that the site currently handles product images, nobody wants to click on even thumbnail to see the product. http://tolvasecuredoors.com/products/personnel-doors/

Totally open to suggestions on layout to enable the feeling outlined in the brief above.

Please ask if anything is not clear or you need answers to drill down on specifics.

Sick

Target Market(s)

Businesses that buy steel doors

Font styles to use
Sans Serif
Other font styles liked:
• Copperplate Gothic Bold - For Company Name but we are open to suggestions

Colors

Designer to choose colors to be used in the design.

Requirements
Must have
• Professional looking, clean design
• Conveys strength, power and weight to represent the quality of the products, the characteristics of steel and the security that they provide.
• Incorporates black and yellow stripes of our branding
• Ability to create pages with content as seen at www.tolvasecuredoors.com
• A better way of showing the product images
Nice to have
• If possible. a design that gives off the feeling that not only do we supply the products we also make them in house too. I don't know what this looks like but a way of differentiating between a supply only business and one that manufacturers the product too.
Should not have
• We don't like the current thumbnail method of showing the product images

```html
<!DOCTYPE html>
<html lang="en">
<head>
<meta charset="utf-8">
<title>Tolvane Engineering Ltd – Personal Doors</title>
<link href="https://fonts.googleapis.com/css2?family=Poppins:wght@300;400;500;600&family=Roboto:wght@400;500&display=swap" rel="stylesheet">
<style>
  :root {
    --ink: #222428;
    --header: #2a2b2f;
    --yellow: #fff200;
    --teal: #4b9895;
    --teal-text: #3d8c89;
    --panel: #f1f1f1;
    --line: #d9d9d9;
    --footer: #1d2a36;
    --footer-base: #14191e;
    --placeholder: #cfcfcf;
    --white: #ffffff;
  }
  * { box-sizing: border-box; margin: 0; padding: 0; }
  html, body { width: 1200px; height: 3750px; overflow: hidden; }
  body { position: relative; background: var(--white); color: var(--ink); font-family: "Roboto", Arial, sans-serif; }

  /* Header */
  .site-header { position: absolute; left: 0; top: 0; width: 1200px; height: 68px; background: var(--header); }
  .brand { position: absolute; left: 88px; top: 14px; display: flex; align-items: center; gap: 10px; }
  .brand-mark { width: 28px; height: 28px; background: var(--teal); }
  .brand-name { font-family: "Poppins", sans-serif; font-weight: 600; color: var(--white); font-size: 17px; line-height: 17px; letter-spacing: 1px; }
  .brand-name small { display: block; font-size: 9px; line-height: 12px; letter-spacing: 1.4px; }
  .main-nav a { position: absolute; top: 0; height: 68px; line-height: 68px; font-family: "Roboto", sans-serif; font-size: 11px; color: var(--white); text-decoration: none; letter-spacing: .5px; }
  .main-nav .is-active { background: var(--yellow); color: var(--ink); text-align: center; }
  .btn-download { position: absolute; left: 842px; top: 24px; width: 128px; height: 24px; background: var(--teal); color: var(--white); font-size: 11px; line-height: 24px; text-align: center; letter-spacing: .5px; }
  .social { position: absolute; top: 24px; display: flex; gap: 7px; }
  .social span { width: 20px; height: 20px; border-radius: 4px; display: block; }

  /* Dropdown */
  .dropdown { position: absolute; left: 600px; top: 68px; width: 242px; height: 207px; background: var(--yellow); font-size: 9.5px; color: var(--ink); }
  .dropdown .col-left { position: absolute; left: 20px; top: 14px; line-height: 20px; list-style: none; }
  .dropdown .col-left li { width: 70px; display: flex; justify-content: space-between; }
  .dropdown .col-right { position: absolute; left: 122px; top: 14px; width: 110px; line-height: 19px; list-style: none; }
  .dropdown .col-right li::before { content: "• "; }

  /* Hero */
  .hero { position: absolute; left: 0; top: 68px; width: 1200px; height: 530px;
    background: linear-gradient(100deg, #3a3433 0%, #6b625c 22%, #4d4a49 45%, #8a7a68 68%, #2f2c2a 100%); }
  .hero-caption { position: absolute; left: 795px; top: 388px; width: 405px; height: 150px; background: rgba(20,20,20,.72); color: var(--white); font-family: "Poppins", sans-serif; text-align: right; padding: 14px 42px 0 0; }
  .hero-caption .kicker { font-size: 21px; font-weight: 400; letter-spacing: 1px; line-height: 30px; }
  .hero-caption .title { font-size: 38px; font-weight: 400; line-height: 44px; }
  .hazard-band { position: absolute; left: 0; top: 583px; width: 1200px; height: 26px; }

  /* Intro */
  .section-title { position: absolute; left: 0; width: 1200px; text-align: center; font-family: "Poppins", sans-serif; font-weight: 600; font-size: 50px; color: var(--ink); }
  .intro { position: absolute; left: 0; width: 1200px; text-align: center; font-size: 16px; line-height: 25px; color: var(--ink); }
  .applications { position: absolute; left: 0; top: 890px; width: 1200px; text-align: center; font-size: 19px; color: var(--teal-text); font-weight: 500; }
  .applications span { margin: 0 12px; }

  /* Product cards */
  .card { position: absolute; width: 250px; }
  .card-photo { width: 250px; height: 190px; }
  .card h3 { margin-top: 17px; font-family: "Roboto", sans-serif; font-weight: 500; font-size: 15px; color: var(--teal-text); }
  .card p { margin-top: 14px; font-size: 12.5px; line-height: 22px; color: var(--ink); }

  /* Spec tabs */
  .spec-tabs { position: absolute; left: 180px; top: 1815px; width: 238px; list-style: none; }
  .spec-tabs li { height: 41px; line-height: 40px; padding-left: 20px; font-size: 11.5px; border: 1px solid var(--line); border-top: none; color: var(--ink); }
  .spec-tabs li.is-active { background: var(--teal); color: var(--white); border-color: var(--teal); }
  .spec-panel { position: absolute; left: 450px; top: 1815px; width: 570px; height: 428px; background: var(--panel); padding: 16px 40px; font-size: 12px; line-height: 15.6px; color: var(--ink); }
  .spec-panel ul { list-style: none; }
  .spec-panel li::before { content: "• "; }
  .spec-panel .gap { height: 15.6px; }

  /* Promo banner */
  .promo { position: absolute; left: 0; top: 2313px; width: 1200px; height: 462px;
    background: linear-gradient(180deg, #27344b 0%, #2e3d58 60%, #39465a 78%, #5a6068 100%); }
  .promo-title { position: absolute; left: 0; top: 2456px; width: 1200px; text-align: center; font-family: "Poppins", sans-serif; font-weight: 600; font-size: 54px; line-height: 70px; color: var(--yellow); }
  .promo-text { position: absolute; left: 0; top: 2534px; width: 1200px; text-align: center; font-size: 13px; line-height: 20px; color: var(--white); }
  .btn-order { position: absolute; left: 519px; top: 2604px; width: 162px; height: 30px; border: 1px solid var(--white); color: var(--white); font-size: 12px; line-height: 28px; text-align: center; letter-spacing: .5px; }

  /* Our products */
  .tile { position: absolute; width: 260px; height: 262px; display: flex; align-items: center; justify-content: center; font-family: "Poppins", sans-serif; font-size: 20px; color: var(--ink); text-align: center; }
  .tile.placeholder { background: var(--placeholder); }
  .tile.feature { color: var(--white); font-weight: 500; line-height: 30px; }

  /* Footer */
  .site-footer { position: absolute; left: 0; top: 3570px; width: 1200px; height: 136px; background: var(--footer); }
  .footer-brand { position: absolute; left: 162px; top: 44px; display: flex; align-items: center; gap: 10px; }
  .footer-address { position: absolute; left: 380px; top: 44px; width: 260px; text-align: center; color: var(--white); font-size: 17px; line-height: 25px; font-style: normal; }
  .badges { position: absolute; left: 732px; top: 40px; display: flex; gap: 6px; }
  .badges span { display: block; height: 54px; }
  .footer-base { position: absolute; left: 0; top: 3706px; width: 1200px; height: 44px; background: var(--footer-base); }
  .copyright { position: absolute; left: 162px; top: 15px; font-size: 10px; color: var(--white); }
</style>
</head>
<body>

<header class="site-header">
  <div class="brand">
    <span class="brand-mark"></span>
    <div class="brand-name">TOLVANE<small>ENGINEERING LTD.</small></div>
  </div>
  <nav class="main-nav">
    <a style="left:538px;">HOME</a>
    <a class="is-active" style="left:600px;width:105px;">PRODUCTS</a>
    <a style="left:730px;">CONTACT</a>
  </nav>
  <div class="btn-download">DOWNLOAD</div>
  <div class="social" style="left:1000px;">
    <span style="background:#3b5a9a"></span>
    <span style="background:#2fa3dc"></span>
    <span style="background:#d9433a"></span>
    <span style="background:#e2406f"></span>
  </div>
</header>

<section class="hero" role="img" aria-label="Modern open-plan living room with sofa, coffee table and floor-to-ceiling windows"></section>
<div class="hero-caption">
  <div class="kicker">TOLVANE ENGINEERING,</div>
  <div class="title">Your Trusted<br>Door Security</div>
</div>
<svg class="hazard-band" viewBox="0 0 1200 26" aria-hidden="true">
  <rect width="1200" height="26" fill="#161616"/>
  <g fill="#fff200">
    <polygon points="130,0 260,0 245,26 115,26"/>
    <polygon points="395,0 525,0 510,26 380,26"/>
    <polygon points="660,0 790,0 775,26 645,26"/>
    <polygon points="925,0 1055,0 1040,26 910,26"/>
  </g>
</svg>

<div class="dropdown">
  <ul class="col-left">
    <li><span>Products</span><span>›</span></li>
    <li><span>Accessories</span><span>›</span></li>
  </ul>
  <ul class="col-right">
    <li>Personnel Doors</li>
    <li>Fire Exit Doors</li>
    <li>Blank Doors</li>
    <li>Acoustic Doors</li>
    <li>Anti-vandal shutters and glazing uni</li>
    <li>Technical Manuals</li>
  </ul>
</div>

<h1 class="section-title" style="top:682px;">Personal Doors</h1>
<p class="intro" style="top:766px;">Tolvane steel security doors are the ideal solution for a wide range of applications<br>in which security, quality and cost are all essential requirements.</p>
<p class="intro" style="top:842px;">Since 1998 Tolvane security doors have been specified extensively for a wide range of applications including:</p>
<p class="applications">Anti-vandal steel cabins<span>|</span>Modular buildings<span>|</span>Steel framed buildings<span>|</span>General building projects</p>
<p class="intro" style="top:922px;">Continuous product development, extensive quality control and our market experience means that we can offer<br>the highest specification steel security door for its price in the UK.</p>

<article class="card" style="left:180px;top:1040px;">
  <div class="card-photo" role="img" aria-label="Door edge showing ten point locking system" style="background:linear-gradient(90deg,#1c1b1b 0%,#7a1a1c 45%,#2a2222 70%,#d8c22a 100%);"></div>
  <h3>10 Point Front Expanded Text</h3>
  <p>Lorem Ipsum is simply dummy text of the printing and typesetting industry. Lorem Ipsum has been the industry's standard dummy text ever since the 1500s.</p>
</article>
<article class="card" style="left:475px;top:1040px;">
  <div class="card-photo" role="img" aria-label="Red steel door with lever handle" style="background:linear-gradient(90deg,#c8111c 0%,#e01f26 55%,#8f0d14 100%);"></div>
  <h3>Red Door Handle</h3>
  <p>Lorem Ipsum is simply dummy text of the printing and typesetting industry. Lorem Ipsum has been the industry's standard dummy text ever since the 1500s.</p>
</article>
<article class="card" style="left:770px;top:1040px;">
  <div class="card-photo" role="img" aria-label="Blue steel door with vision panel, front view" style="background:linear-gradient(180deg,#1f4f86 0%,#2a5d96 60%,#1b3f6b 100%);"></div>
  <h3>Bluedoor Front</h3>
  <p>Lorem Ipsum is simply dummy text of the printing and typesetting industry. Lorem Ipsum has been the industry's standard dummy text ever since the 1500s.</p>
</article>
<article class="card" style="left:180px;top:1413px;">
  <div class="card-photo" role="img" aria-label="Red slatted steel door with handle" style="background:linear-gradient(90deg,#d3141d 0%,#ec2a2f 60%,#b20f17 100%);"></div>
  <h3>Red Door Slatted</h3>
  <p>Lorem Ipsum is simply dummy text of the printing and typesetting industry. Lorem Ipsum has been the industry's standard dummy text ever since the 1500s.</p>
</article>
<article class="card" style="left:475px;top:1413px;">
  <div class="card-photo" role="img" aria-label="White steel site cabin with doors" style="background:linear-gradient(180deg,#f4f4f4 0%,#dedede 70%,#bdbdbd 100%);"></div>
  <h3>Cabin</h3>
  <p>Lorem Ipsum is simply dummy text of the printing and typesetting industry. Lorem Ipsum has been the industry's standard dummy text ever since the 1500s.</p>
</article>
<article class="card" style="left:770px;top:1413px;">
  <div class="card-photo" role="img" aria-label="Grey double external steel door" style="background:linear-gradient(180deg,#6b7a86 0%,#5c6a75 100%);"></div>
  <h3>External Door</h3>
  <p>Lorem Ipsum is simply dummy text of the printing and typesetting industry. Lorem Ipsum has been the industry's standard dummy text ever since the 1500s.</p>
</article>

<ul class="spec-tabs">
  <li class="is-active">DOOR CONSTRUCTION</li>
  <li>STANDARD FEATURES</li>
  <li>CERTIFICATION &amp; TESTING</li>
  <li>THRESHOLD SPECIFICATION</li>
  <li>SIZE SPECIFICATION</li>
  <li>INTERNAL/EXTERNAL OPENING</li>
  <li>ACCESSORIES</li>
</ul>
<div class="spec-panel">
  <p>Tolvane steel security doors are designed and manufactured to the highest standards:</p>
  <ul>
    <li>Door skins – 1mm primed galvanised steel</li>
    <li>Frame – 2mm primed galvanised steel</li>
    <li>Threshold – stainless steel</li>
    <li>Door and frame profile – Rebated to produce a natural astragal</li>
    <li>Anti-vandal specification – Extra anti-jemmy flange available on 910x2065mm &amp;<br>&nbsp;&nbsp;1110x2065mm sizes</li>
  </ul>
  <div class="gap"></div>
  <p>The internal construction of a Tolvane steel door sets it apart from the competition.</p>
  <div class="gap"></div>
  <p>Tolvane security doors are designed and built to last:</p>
  <ul>
    <li>Door leaf insulation – Polyurethane foam injection</li>
    <li>Door frame insulation – Polyurethane foam injection</li>
    <li>Steel subframe and strengtheners</li>
    <li>4mm roundbar steel mesh throughout the door</li>
    <li>3mm steel backing plates for auxiliary furniture fixing</li>
    <li>2mm steel lock protection box</li>
    <li>Anti-drill plates</li>
    <li>Stainless steel locking rod tube</li>
    <li>Galvanised steel locking rods</li>
  </ul>
</div>

<section class="promo" role="img" aria-label="Navy-walled room with wooden sliding barn door, chest of drawers and table lamp"></section>
<h2 class="promo-title">Loren Ipsum Door</h2>
<p class="promo-text">Lorem Ipsum is simply dummy text of the printing and typesetting industry. Lorem<br>Ipsum has been the industry's standard dummy text ever since the 1500s.</p>
<div class="btn-order">ORDER NOW!</div>

<h2 class="section-title" style="top:2825px;">Our Products</h2>
<div class="tile feature" style="left:185px;top:2940px;background:linear-gradient(90deg,#a80f17 0%,#d41b22 50%,#9a0d14 100%);" role="img" aria-label="Red slatted personnel door">Personnel<br>Doors</div>
<div class="tile" style="left:470px;top:2940px;background:linear-gradient(180deg,#f2f2f2 0%,#dcdcdc 100%);" role="img" aria-label="White fire exit door with push bar"></div>
<div class="tile placeholder" style="left:755px;top:2940px;">Photo</div>
<div class="tile placeholder" style="left:185px;top:3225px;">Photo</div>
<div class="tile" style="left:470px;top:3225px;background:linear-gradient(180deg,#a9acae 0%,#8f9396 100%);" role="img" aria-label="Grey double steel doors"></div>
<div class="tile placeholder" style="left:755px;top:3225px;">Photo</div>

<footer class="site-footer">
  <div class="footer-brand">
    <span class="brand-mark"></span>
    <div class="brand-name">TOLVANE<small>ENGINEERING LTD.</small></div>
  </div>
  <address class="footer-address">Marsden Row, Elstow,<br>Hull, HU14 3QD</address>
  <div class="badges">
    <span style="width:60px;background:#e8e8ea;"></span>
    <span style="width:60px;background:#f0f0f0;"></span>
    <span style="width:58px;background:#b5662e;"></span>
  </div>
</footer>
<div class="footer-base">
  <p class="copyright">© Copyright 2018 &nbsp;|&nbsp; TOLVANE ENGINEERING</p>
  <div class="social" style="left:1000px;top:12px;">
    <span style="background:#3b5a9a"></span>
    <span style="background:#2fa3dc"></span>
    <span style="background:#d9433a"></span>
    <span style="background:#e2406f"></span>
  </div>
</div>

</body>
</html>
```